BrivoMatex. Lantern for the Steady Growth. Business card

Professional business card for BrivoMatex (Lantern for the Steady Growth)
My rationale: Strategy-> Execution-> Results-> Value that lead to the BrivoMatex name: We put the Lantern for the Steady Growth.
We deliver value to our customers helping them at defining a good strategy (cyan arrow). 90% of well formulated strategies fail due to poor execution so we also consider strategical execution very important (green arrow). Due to the execution we obtain the results (blue arrow). Finally, the results provide feedback to redefine strategy, and the new strategy has to be executed and new results obtained providing new feedback and on and on. It's like a wheel that finally, must create corporate value: value for shareholders, staholders, employees, providers...-

Target Market(s)

CEOs and steering comitees , invewrnent funds

Industry/Entity Type

Business Consultant

Contact Information for Business Card

Tommaso Ferlini
CEO & Founder
tommaso.ferlini@brivomatex.example
Mobile: +34 611.205.938
www.brivomatex.example

Colors

Designer to choose colors to be used in the design.

Requirements
Nice to have
• Nice to hace the words: Strategy, execution, results
• Nice to vave the claim: Lantern for the Steady Growth
• The three colors should be shown:
• cyan for STRATEGY
• green for EXECUTION
• blue for RESULTS
Should not have
• Complete black background

```html
<!DOCTYPE html>
<html lang="en">
<head>
<meta charset="utf-8">
<title>BrivoMatex – Business Card</title>
<link rel="stylesheet" href="https://fonts.googleapis.com/css2?family=Open+Sans:wght@400;600;700&display=swap">
<style>
  :root {
    --navy: #233f94;
    --green: #8dc63f;
    --cyan: #29abe2;
    --ink: #454545;
    --paper: #ffffff;
    --backdrop: #e6e8ec;
  }
  * { margin: 0; padding: 0; box-sizing: border-box; }
  html, body {
    width: 1200px;
    height: 1000px;
    overflow: hidden;
    background: var(--backdrop);
    font-family: "Open Sans", Arial, sans-serif;
  }
  .sheet {
    position: relative;
    width: 1200px;
    height: 1000px;
  }
  .card {
    position: absolute;
    left: 260px;
    width: 680px;
    height: 390px;
    border-radius: 22px;
    overflow: hidden;
    box-shadow: 0 10px 28px rgba(20, 30, 60, 0.22);
  }
  .card--front {
    top: 90px;
    background: var(--navy);
    display: flex;
    align-items: center;
    justify-content: center;
  }
  .card--back {
    top: 520px;
    background: var(--paper);
  }
  .wordmark {
    font-weight: 700;
    letter-spacing: -1px;
    line-height: 1;
  }
  .card--front .wordmark {
    color: var(--paper);
    font-size: 82px;
  }
  .card--back .wordmark {
    position: absolute;
    right: 48px;
    top: 150px;
    color: var(--navy);
    font-size: 54px;
  }
  .contact {
    position: absolute;
    left: 48px;
    top: 88px;
  }
  .contact__name {
    color: var(--green);
    font-weight: 700;
    font-size: 27px;
    letter-spacing: 0.5px;
  }
  .contact__role {
    color: var(--ink);
    font-size: 17px;
    margin-top: 2px;
  }
  .contact__list {
    list-style: none;
    margin-top: 20px;
  }
  .contact__list li {
    display: flex;
    align-items: center;
    gap: 10px;
    color: var(--ink);
    font-size: 17px;
    line-height: 1.75;
  }
  .contact__list svg {
    width: 15px;
    height: 15px;
    flex: none;
    fill: var(--navy);
  }
  .swoosh {
    position: absolute;
    left: 0;
    bottom: 0;
    width: 680px;
    height: 390px;
  }
</style>
</head>
<body>
<main class="sheet">
  <section class="card card--front" aria-label="Card front">
    <span class="wordmark">BrivoMatex</span>
  </section>

  <section class="card card--back" aria-label="Card back">
    <svg class="swoosh" viewBox="0 0 680 390" aria-hidden="true">
      <defs>
        <linearGradient id="fade-navy" x1="0" y1="0" x2="1" y2="0">
          <stop offset="0" stop-color="#233f94" stop-opacity="0"/>
          <stop offset="1" stop-color="#233f94" stop-opacity="1"/>
        </linearGradient>
      </defs>
      <path d="M0 300 C 110 340, 280 345, 470 352 C 560 356, 640 330, 680 300 L 680 390 L 0 390 Z" fill="var(--navy)"/>
      <path d="M0 282 C 110 330, 280 336, 470 348 C 400 344, 260 340, 140 318 C 80 306, 30 294, 0 282 Z" fill="var(--green)"/>
      <path d="M150 292 C 300 300, 470 310, 560 340 C 620 330, 660 315, 680 300 C 620 320, 560 320, 480 312 C 360 300, 250 296, 150 292 Z" fill="url(#fade-navy)"/>
    </svg>

    <div class="contact">
      <h1 class="contact__name">Tommaso Ferlini</h1>
      <p class="contact__role">CEO &amp; Founder</p>
      <ul class="contact__list">
        <li>
          <svg viewBox="0 0 16 16"><path d="M4 0h8a1.5 1.5 0 0 1 1.5 1.5v13A1.5 1.5 0 0 1 12 16H4a1.5 1.5 0 0 1-1.5-1.5v-13A1.5 1.5 0 0 1 4 0zm0 2v10h8V2zm4 11a1 1 0 1 0 0 2 1 1 0 0 0 0-2z"/></svg>
          +34 611.205.938
        </li>
        <li>
          <svg viewBox="0 0 16 16"><path d="M0 3h16v1.2L8 9 0 4.2zM0 5.8l8 4.8 8-4.8V13H0z"/></svg>
          tommaso.ferlini@brivomatex.example
        </li>
        <li>
          <svg viewBox="0 0 16 16"><path d="M8 0a8 8 0 1 0 0 16A8 8 0 0 0 8 0zm5.9 7h-2.6a12 12 0 0 0-1-4.6A6 6 0 0 1 13.9 7zM8 2.1c.7.9 1.2 2.7 1.3 4.9H6.7C6.8 4.8 7.3 3 8 2.1zM5.7 2.4a12 12 0 0 0-1 4.6H2.1a6 6 0 0 1 3.6-4.6zM2.1 9h2.6a12 12 0 0 0 1 4.6A6 6 0 0 1 2.1 9zM8 13.9c-.7-.9-1.2-2.7-1.3-4.9h2.6c-.1 2.2-.6 4-1.3 4.9zm2.3-.3a12 12 0 0 0 1-4.6h2.6a6 6 0 0 1-3.6 4.6z"/></svg>
          www.brivomatex.example
        </li>
      </ul>
    </div>

    <span class="wordmark">BrivoMatex</span>
  </section>
</main>
</body>
</html>
```